Property Management business needs Business cards designed

We provide a premium property management service based in Sydney's Norther Beaches. We want people to feel confident in choosing us to manage their investment properties. We offer a much more personalized service than other estate agents.
We want a modern clean design. Something that shows confidence without being complicated.
Logo attached.

Target Market(s)

35-70yo Male and Female with strong property portfolios within Sydney's Norther Beaches

Industry/Entity Type

Property Management

Contact Information for Business Card

Address: Suite 7, 12-14 Kelvin Parade, Harlow NSW 2188
Two separate named cards.
Tom Ardley - 0491 570 118 tom@harbourvaleestates.com.au
Clara Dunmore - 0491 570 263 clara@harbourvaleestates.com.au

Requirements
Must have
• Business logo, name, number, address, email.

```html
<!DOCTYPE html>
<html lang="en">
<head>
<meta charset="utf-8">
<title>Harbourvale Estates – Business Cards</title>
<link rel="stylesheet" href="https://fonts.googleapis.com/css2?family=Arimo:wght@400;700&display=swap">
<style>
  :root {
    --page: #e9ebec;
    --teal: #1a7480;
    --teal-deep: #0f5a66;
    --teal-light: #2f8e99;
    --ink: #111416;
    --text: #3c4246;
    --white: #ffffff;
    --card-w: 540px;
    --card-h: 330px;
  }
  * { box-sizing: border-box; margin: 0; padding: 0; }
  html, body {
    width: 1200px; height: 950px; overflow: hidden;
    background: var(--page);
    font-family: "Arimo", Arial, sans-serif;
  }
  .canvas {
    width: 1200px; height: 950px;
    display: flex; flex-direction: column; align-items: center; justify-content: center; gap: 40px;
  }
  .card-row { display: flex; gap: 40px; }
  .card {
    position: relative;
    width: var(--card-w); height: var(--card-h);
    border-radius: 4px; overflow: hidden;
    box-shadow: 0 10px 28px rgba(0,0,0,.18);
  }

  /* Back */
  .card--back {
    background: linear-gradient(100deg, var(--teal-deep) 0%, var(--teal) 50%, var(--teal-deep) 100%);
  }
  .back-band {
    position: absolute; top: 0; bottom: 0; right: 78px; width: 90px;
    background: linear-gradient(90deg, rgba(255,255,255,0) 0%, rgba(255,255,255,.16) 45%, rgba(255,255,255,.06) 100%);
  }
  .back-brand {
    position: absolute; left: 0; right: 0; top: 118px;
    display: flex; align-items: center; justify-content: center; gap: 14px;
    color: var(--white); font-weight: 700; font-size: 30px; letter-spacing: .5px;
  }
  .back-brand .mark { width: 22px; height: 22px; border-radius: 50%; background: var(--white); }
  .back-web {
    position: absolute; right: 24px; bottom: 24px;
    color: rgba(255,255,255,.75); font-size: 15px; letter-spacing: 2.5px;
  }

  /* Front */
  .card--front { background: linear-gradient(180deg, #ffffff 0%, #f2f3f3 100%); }
  .brand {
    position: absolute; left: 34px; top: 36px;
    display: flex; align-items: center; gap: 10px;
    color: var(--ink); font-weight: 700; font-size: 30px; letter-spacing: -.3px;
  }
  .brand .mark { width: 18px; height: 18px; border-radius: 50%; background: var(--teal); }
  .details {
    position: absolute; left: 34px; top: 112px;
    color: var(--text); font-size: 15px; line-height: 1.35;
  }
  .address { margin-bottom: 4px; }
  .contact-row { display: flex; align-items: center; gap: 7px; }
  .contact-row svg { width: 13px; height: 13px; fill: var(--teal); flex: none; }
  .name-tab {
    position: absolute; right: 0; bottom: 30px;
    width: 236px; height: 56px;
    background: linear-gradient(90deg, var(--teal-light) 0%, var(--teal) 60%, var(--teal-deep) 100%);
    display: flex; align-items: center;
  }
  .name-tab .texture { width: 26px; height: 100%; background: linear-gradient(90deg, #5aaab3, var(--teal-light)); }
  .name-tab .name {
    flex: 1; text-align: center; padding-right: 10px;
    color: var(--white); font-size: 19px; font-weight: 700;
  }
</style>
</head>
<body>
<main class="canvas">
  <div class="card-row">
    <section class="card card--back" aria-label="Card back">
      <div class="back-band" role="img" aria-label="Soft textured light band"></div>
      <div class="back-brand"><span class="mark"></span>Harbourvale Estates</div>
      <div class="back-web">harbourvaleestates.com.au</div>
    </section>
  </div>

  <div class="card-row">
    <section class="card card--front" aria-label="Card front, Tom Ardley">
      <div class="brand"><span class="mark"></span>Harbourvale Estates</div>
      <div class="details">
        <p class="address">Suite 7, 12-14 Kelvin Parade<br>Harlow NSW 2188</p>
        <p class="contact-row">
          <svg viewBox="0 0 16 16" aria-hidden="true"><path d="M3 1h3l1.5 4-2 1.2a9 9 0 0 0 4.3 4.3L11 8.5l4 1.5v3a2 2 0 0 1-2 2C6.9 15 1 9.1 1 3a2 2 0 0 1 2-2z"/></svg>
          0491 570 118
        </p>
        <p class="contact-row">
          <svg viewBox="0 0 16 16" aria-hidden="true"><path d="M1 3h14v10H1z M1 3l7 5 7-5" stroke="#fff" stroke-width="1.2"/></svg>
          tom@harbourvaleestates.com.au
        </p>
        <p class="contact-row">
          <svg viewBox="0 0 16 16" aria-hidden="true"><circle cx="8" cy="8" r="7"/><path d="M1 8h14M8 1c-3 4-3 10 0 14M8 1c3 4 3 10 0 14" stroke="#fff" stroke-width="1" fill="none"/></svg>
          www.harbourvaleestates.com.au
        </p>
      </div>
      <div class="name-tab">
        <div class="texture" role="img" aria-label="Soft textured edge"></div>
        <span class="name">Tom Ardley</span>
      </div>
    </section>

    <section class="card card--front" aria-label="Card front, Clara Dunmore">
      <div class="brand"><span class="mark"></span>Harbourvale Estates</div>
      <div class="details">
        <p class="address">Suite 7, 12-14 Kelvin Parade<br>Harlow NSW 2188</p>
        <p class="contact-row">
          <svg viewBox="0 0 16 16" aria-hidden="true"><path d="M3 1h3l1.5 4-2 1.2a9 9 0 0 0 4.3 4.3L11 8.5l4 1.5v3a2 2 0 0 1-2 2C6.9 15 1 9.1 1 3a2 2 0 0 1 2-2z"/></svg>
          0491 570 263
        </p>
        <p class="contact-row">
          <svg viewBox="0 0 16 16" aria-hidden="true"><path d="M1 3h14v10H1z M1 3l7 5 7-5" stroke="#fff" stroke-width="1.2"/></svg>
          clara@harbourvaleestates.com.au
        </p>
        <p class="contact-row">
          <svg viewBox="0 0 16 16" aria-hidden="true"><circle cx="8" cy="8" r="7"/><path d="M1 8h14M8 1c-3 4-3 10 0 14M8 1c3 4 3 10 0 14" stroke="#fff" stroke-width="1" fill="none"/></svg>
          www.harbourvaleestates.com.au
        </p>
      </div>
      <div class="name-tab">
        <div class="texture" role="img" aria-label="Soft textured edge"></div>
        <span class="name">Clara Dunmore</span>
      </div>
    </section>
  </div>
</main>
</body>
</html>
```